Adult Literacy Program - flyer to attract volunteers and students

We want a flyer that is engaging, colorful, modern and will appeal to our primary audience of adults aged 40-60. We are trying to attract both prospective volunteers (typically age 50+, mostly women) and students (typically aged 40+).
The flyer should feature diverse people working together in pairs of two, reading or talking, with a workbook or some reading material in front of them.

Our organization trains tutors to work one-on-one with adults who are learning how to read. Most of our adult students are non-native speakers of English. Many are of Haitian or Hispanic origin, so we would like some people who represent that demographic.

The Flyer should represent reading, learning, literacy, knowledge, growth,
and opportunities.
Our students are learning to read so they can advance their job opportunities.

Target Market(s)

Adults aged 40-60, primarily women, retired, volunteers

Industry/Entity Type

Education

Font styles to use
Serif
Sans Serif

Colors

Designer to choose colors to be used in the design.

Requirements
Must have
• - UPDATE: Should be designed as a TRI-FOLD brochure on 8.5 x 11 inch paper that will be folded into thirds.
• - Images of diverse people, women and men, who look Hispanic, Haitian and other nationalities as well as Caucasian.
• - Our logo on the front cover
Nice to have
• The sample flyer is very boring and dry! We are open to different ways of presenting the text.

```html
<!DOCTYPE html>
<html lang="en">
<head>
<meta charset="utf-8">
<title>Adult Literacy Tri-fold Brochure</title>
<link href="https://fonts.googleapis.com/css2?family=Open+Sans:wght@300;400;600;700;800&family=Marck+Script&display=swap" rel="stylesheet">
<style>
  :root {
    --stage: #3a3a3a;
    --green: #00f57f;
    --cyan: #00f2ec;
    --navy: #0b1f66;
    --deep-navy: #06067f;
    --paper: #f2f2f2;
    --warm-paper: #e8e5e1;
    --white: #ffffff;
    --ink: #111111;
    --photo-a: #c9b8a8;
    --photo-b: #8f7d70;
    --book-a: #1ba3e0;
    --book-b: #0d2a6e;
  }
  * { margin: 0; padding: 0; box-sizing: border-box; }
  html, body { width: 786px; height: 1200px; overflow: hidden; background: var(--stage); }
  body { position: relative; font-family: "Open Sans", Arial, sans-serif; color: var(--ink); }
  .sheet { position: absolute; left: 100px; width: 588px; height: 454px; overflow: hidden; }
  .sheet--outside { top: 109px; background: var(--warm-paper); }
  .sheet--inside { top: 613px; height: 454px; background: var(--paper); }
  .abs { position: absolute; }
  .center { text-align: center; }
  .backdrop { position: absolute; left: 0; top: 0; }

  /* outside: cover panel */
  .cover-box { left: 0; top: 0; width: 196px; height: 291px; background: var(--white);
    border-right: 6px solid var(--cyan); border-bottom: 6px solid var(--cyan); }
  .cover-title { left: 0; top: 10px; width: 190px; font-weight: 800; font-size: 26px; line-height: 38px;
    color: var(--navy); letter-spacing: 1px; }
  .book-mark { border-radius: 40% 40% 8px 8px; background: linear-gradient(160deg, var(--book-a), var(--book-b)); opacity: .9; }
  .cover-tag { left: 0; top: 213px; width: 190px; font-weight: 700; font-size: 14.5px; line-height: 22px; }
  .cover-points { left: 0; top: 291px; width: 196px; height: 163px; background: var(--green);
    padding: 18px 8px 0 18px; list-style: none; font-weight: 700; font-size: 11px; line-height: 22.4px; }
  .cover-points li { position: relative; padding-left: 5px; }
  .cover-points li::before { content: "•"; position: absolute; left: -5px; }

  .contact { left: 196px; width: 196px; font-weight: 700; font-size: 14px; line-height: 22px; color: var(--ink); }
  .contact--small { font-size: 11.5px; }
  .url-bar { top: 544px; height: 18px; width: 195px; background: var(--warm-paper); font-weight: 700;
    font-size: 10.5px; line-height: 18px; padding-left: 14px; }

  .photo-ring { border-radius: 50%; overflow: hidden; }
  .photo { width: 100%; height: 100%; border-radius: 50%; background: radial-gradient(circle at 40% 40%, var(--photo-a), var(--photo-b)); }

  .motto { left: 392px; top: 382px; width: 196px; font-family: "Marck Script", cursive; font-size: 22px; color: var(--navy); }

  /* inside */
  .band { top: 0; }
  .panel-heading { font-weight: 700; font-size: 17px; letter-spacing: .5px; width: 196px; }
  .panel-copy { font-weight: 600; font-size: 14px; line-height: 18px; width: 196px; }
  .list { list-style: none; font-weight: 300; font-size: 9.4px; line-height: 17.8px; color: #222; }
  .list li::before { content: "•"; margin-right: 2px; }
  .list .sub { padding-left: 27px; }
  .callout { font-weight: 700; font-size: 10.8px; line-height: 18px; width: 196px; }
  .url { font-weight: 700; font-size: 9.6px; width: 196px; }
  .badge { left: 52px; top: 349px; width: 92px; height: 68px; background: var(--white);
    display: flex; align-items: center; justify-content: center; gap: 5px; padding: 4px; }
  .badge-dot { width: 14px; height: 14px; border-radius: 50%; background: var(--navy); flex: none; }
  .badge-name { font-weight: 700; font-size: 9.5px; line-height: 12px; color: var(--navy); }
</style>
</head>
<body>

<!-- Outside sheet: cover, contact panel, back panel -->
<section class="sheet sheet--outside">
  <svg class="backdrop" width="588" height="454" viewBox="0 0 588 454">
    <polygon points="196,96 322,2 588,205 588,454 196,454" fill="var(--cyan)"/>
    <polygon points="196,118 322,24 588,228 588,454 196,454" fill="var(--navy)"/>
    <polygon points="196,140 322,46 588,256 588,454 196,454" fill="var(--green)"/>
    <polygon points="196,110 322,14 330,20 196,122" fill="var(--white)"/>
  </svg>

  <div class="abs cover-box"></div>
  <svg class="abs" style="left:0;top:0" width="40" height="70" viewBox="0 0 40 70"><polygon points="0,0 40,0 0,66" fill="var(--cyan)"/></svg>
  <h1 class="abs cover-title center">CONNECT<br>INSPIRE<br>ENRICE</h1>
  <div class="abs book-mark" role="img" aria-label="Open book with birds rising from its pages" style="left:42px;top:130px;width:100px;height:85px"></div>
  <p class="abs cover-tag center">A highly rewarding<br>experience awaits<br>you!</p>
  <ul class="abs cover-points">
    <li>Volunteer a few thours each week and make a difference.</li>
    <li>Teach an adult to read, write or speak English.</li>
    <li>Materials and training are offered free-of-charge.</li>
  </ul>

  <div class="abs book-mark" role="img" aria-label="Open book with birds rising from its pages" style="left:248px;top:70px;width:100px;height:85px"></div>
  <p class="abs contact center" style="top:157px">Don’t waste a moment!<br>Contact us today<br>to learn more.</p>
  <p class="abs contact center" style="top:246px">Volunteer Desk<br>555-210-4830</p>
  <p class="abs contact center" style="top:313px">Lakeside, Millbrook &amp;<br>Southport<br>555-318-2290</p>
  <p class="abs contact contact--small center" style="top:379px">email: literacy@ridgelibrary.org</p>

  <div class="abs photo-ring" style="left:498px;top:18px;width:190px;height:190px;background:var(--white);padding:5px">
    <div class="photo-ring" style="width:100%;height:100%;background:var(--cyan);padding:5px">
      <div class="photo" role="img" aria-label="Photo: young woman helping an elderly man read a book"></div>
    </div>
  </div>
  <div class="abs book-mark" role="img" aria-label="Open book with birds rising from its pages" style="left:444px;top:290px;width:96px;height:86px"></div>
  <p class="abs motto center">Learning for life</p>

  <div class="abs url-bar" style="left:196px;top:435px">http://www.ridgelibrary.org</div>
  <div class="abs url-bar" style="left:393px;top:435px">http://www.ridgelibrary.org</div>
</section>

<!-- Inside sheet: volunteer, tutor, student panels -->
<section class="sheet sheet--inside">
  <svg class="backdrop" width="588" height="454" viewBox="0 0 588 454">
    <polygon points="0,0 196,0 196,36 0,234" fill="var(--deep-navy)"/>
    <polygon points="196,36 196,48 0,248 0,234" fill="var(--green)"/>
    <rect x="196" y="0" width="196" height="454" fill="var(--green)"/>
    <polygon points="392,0 588,0 588,167" fill="var(--deep-navy)"/>
    <polygon points="400,0 418,0 588,146 588,160" fill="var(--green)"/>
    <polygon points="392,4 392,12 588,180 588,170" fill="var(--green)"/>
  </svg>

  <!-- volunteer -->
  <div class="abs band" style="left:70px;width:56px;height:80px;background:var(--green)"></div>
  <div class="abs photo-ring" style="left:26px;top:49px;width:144px;height:144px;background:var(--green);padding:7px">
    <div class="photo" role="img" aria-label="Photo: smiling woman and older man reading together"></div>
  </div>
  <h2 class="abs panel-heading center" style="left:0;top:196px">VOLUNTEER</h2>
  <p class="abs panel-copy center" style="left:0;top:244px">Enrich a Life!</p>
  <p class="abs panel-copy center" style="left:2px;top:284px">Help an adult to<br>read, write or<br>speak English</p>
  <div class="abs badge"><span class="badge-dot"></span><span class="badge-name">Ridge County Library</span></div>
  <p class="abs url center" style="left:0;top:434px">http://www.ridgelibrary.org</p>

  <!-- tutor -->
  <div class="abs band" style="left:262px;width:67px;height:80px;background:var(--white)"></div>
  <div class="abs photo-ring" style="left:205px;top:45px;width:180px;height:180px;background:var(--white);padding:10px">
    <div class="photo" role="img" aria-label="Photo: tutor and young man working through a workbook at a table"></div>
  </div>
  <h2 class="abs panel-heading center" style="left:196px;top:225px">TUTORE</h2>
  <ul class="abs list" style="left:204px;top:258px;width:186px">
    <li>No special skills or degrees needed —</li>
    <li style="padding-left:8px;list-style:none" class="nobullet">just &nbsp;a degree of caring!</li>
    <li>Training offered throug hout &nbsp;the year</li>
    <li>Tutors meet students weekly at a library</li>
    <li>Instructional materials provided</li>
    <li>Ongoing support available</li>
  </ul>
  <p class="abs callout center" style="left:196px;top:370px">TEACH AN ADULT TO READ AND<br>YOU’LL CHANGE A LIFE FOREVER.</p>
  <div class="abs" style="left:218px;top:431px;width:141px;height:20px;background:var(--white)"></div>
  <p class="abs url center" style="left:194px;top:434px">http://www.ridgelibrary.org</p>

  <!-- student -->
  <div class="abs band" style="left:465px;width:53px;height:80px;background:var(--green)"></div>
  <div class="abs photo-ring" style="left:418px;top:49px;width:144px;height:144px;background:var(--green);padding:7px">
    <div class="photo" role="img" aria-label="Photo: older couple studying a document together"></div>
  </div>
  <h2 class="abs panel-heading center" style="left:392px;top:196px">STUDENT</h2>
  <ul class="abs list" style="left:404px;top:240px;width:184px">
    <li>Students are adults in need of</li>
    <li class="sub">basic literacy skills</li>
    <li class="sub">pre GED skills</li>
    <li class="sub">conversational English</li>
    <li>Tutoring is free of charge</li>
    <li>Tutoring is one-on-one</li>
    <li>Flexible scheduling during library hours</li>
    <li>Lessons focus on student goals</li>
  </ul>
  <p class="abs callout center" style="left:392px;top:382px">IF YOU CAN READ, YOU CAN TUTOR!</p>
  <p class="abs url center" style="left:392px;top:434px">http://www.ridgelibrary.org</p>
</section>

</body>
</html>
```